Design for product lable
MERO LUX
COMMING SOON
background design for nutrition products
such as whey protein powders Cretin and so on
this well be our background style
all the fallowing products gonna look nearly the same so the wining design well work on all other products we produce background our bottle color is black we have blue and gold on our logo
athlete, mostly fitness and bodybuilders
and all others sports
it must come in 4 flavor variants : chocolate, vanilla, strawberry,banana
pleas avoid using to many braid colors
try to give a royal look to it thank you
remember it is 250 because separately for each product if you are a wining project then we make a deal what we gonna pay for the each fallowing product
amino profile total hight 6cm
weight 12 cm
color wight or must much whit the label color or whit background blact text
this is a bad resolution so pleas make new charts

```html
<!DOCTYPE html>
<html lang="en">
<head>
<meta charset="utf-8">
<title>MERO LUX – Flavor Labels</title>
<link href="https://fonts.googleapis.com/css2?family=Cinzel:wght@400;700&family=Roboto+Condensed:wght@400;700&display=swap" rel="stylesheet">
<style>
  :root {
    --stage: #0d0d0d;
    --stage-glow: #2a2a2a;
    --ink-light: #f4f1ea;
    --ink-muted: #c9c4b8;
    --choc: #6b3512;
    --banana: #a8861c;
    --straw: #8e1a1c;
    --vanilla: #1d3f8a;
    --label-dark: #120a06;
  }
  * { box-sizing: border-box; margin: 0; padding: 0; }
  html, body { width: 1200px; height: 901px; overflow: hidden; }
  body {
    background: radial-gradient(ellipse at 50% 30%, var(--stage-glow) 0%, var(--stage) 65%);
    font-family: "Roboto Condensed", Arial, sans-serif;
    color: var(--ink-light);
  }
  .label-row {
    position: absolute;
    left: 60px;
    top: 290px;
    display: flex;
    gap: 40px;
  }
  .label {
    width: 240px;
    height: 320px;
    border-radius: 4px;
    padding: 22px 16px 16px;
    display: flex;
    flex-direction: column;
    align-items: center;
    text-align: center;
    background: radial-gradient(ellipse at 50% 40%, var(--tone) 0%, var(--label-dark) 95%);
    box-shadow: 0 0 0 1px rgba(255,255,255,0.06);
  }
  .label--chocolate { --tone: var(--choc); }
  .label--banana { --tone: var(--banana); }
  .label--strawberry { --tone: var(--straw); }
  .label--vanilla { --tone: var(--vanilla); }
  .flavor {
    font-size: 12px;
    color: var(--ink-muted);
    letter-spacing: 0.5px;
    height: 16px;
  }
  .brand {
    margin-top: 32px;
    display: flex;
    align-items: center;
    gap: 6px;
  }
  .brand-dot {
    width: 10px; height: 10px; border-radius: 50%;
    background: var(--ink-light);
  }
  .brand-name {
    font-family: "Cinzel", Georgia, serif;
    font-size: 17px;
    font-weight: 400;
    letter-spacing: 1.5px;
    color: var(--ink-light);
  }
  .tagline {
    font-size: 7px;
    letter-spacing: 3px;
    color: var(--ink-muted);
    margin-top: 3px;
    text-transform: uppercase;
  }
  .product-name {
    font-family: "Cinzel", Georgia, serif;
    font-weight: 700;
    font-size: 36px;
    letter-spacing: 1px;
    margin-top: 6px;
    line-height: 1;
    color: var(--ink-light);
  }
  .ingredients {
    margin-top: 8px;
    font-size: 10px;
    font-weight: 700;
    line-height: 1.35;
    text-transform: uppercase;
    text-align: left;
    color: var(--ink-light);
  }
  .net-weight {
    margin-top: auto;
    font-size: 10px;
    color: var(--ink-muted);
    letter-spacing: 0.3px;
  }
</style>
</head>
<body>
  <main class="label-row">
    <section class="label label--chocolate">
      <p class="flavor">Double Rich Chocolate</p>
      <div class="brand"><span class="brand-dot"></span><span class="brand-name">VALORNUTRA</span></div>
      <p class="tagline">built for results</p>
      <h2 class="product-name">MERO LUX</h2>
      <p class="ingredients">• Whey Isolate • Egg Protein Isolate<br>• Calsium Caseinate</p>
      <p class="net-weight">dietary supplement, net wt. 2kg</p>
    </section>
    <section class="label label--banana">
      <p class="flavor">Banana</p>
      <div class="brand"><span class="brand-dot"></span><span class="brand-name">VALORNUTRA</span></div>
      <p class="tagline">built for results</p>
      <h2 class="product-name">MERO LUX</h2>
      <p class="ingredients">• Whey Isolate • Egg Protein Isolate<br>• Calsium Caseinate</p>
      <p class="net-weight">dietary supplement, net wt. 2kg</p>
    </section>
    <section class="label label--strawberry">
      <p class="flavor">Strawberry</p>
      <div class="brand"><span class="brand-dot"></span><span class="brand-name">VALORNUTRA</span></div>
      <p class="tagline">built for results</p>
      <h2 class="product-name">MERO LUX</h2>
      <p class="ingredients">• Whey Isolate • Egg Protein Isolate<br>• Calsium Caseinate</p>
      <p class="net-weight">dietary supplement, net wt. 2kg</p>
    </section>
    <section class="label label--vanilla">
      <p class="flavor">Vanilla</p>
      <div class="brand"><span class="brand-dot"></span><span class="brand-name">VALORNUTRA</span></div>
      <p class="tagline">built for results</p>
      <h2 class="product-name">MERO LUX</h2>
      <p class="ingredients">• Whey Isolate • Egg Protein Isolate<br>• Calsium Caseinate</p>
      <p class="net-weight">dietary supplement, net wt. 2kg</p>
    </section>
  </main>
</body>
</html>
```